bramblewood mental health web page

this is to be a single page with no links - will function just like an add.
will have 2 biographies
contact info.
Updates

Dear Designers - most of these are too complex.

 Just want one page with contact details (yet to be sorted). No email contact as we can't monitor all emails and if person emails saying suicidal I am potentially accountable if they are successful. Hence- this is just like a listing in a phone book. 
2 photos - one of me the other my husband - with a little blurb next to our names.
No info on fees or appointments etc
I am legally not allowed use language like - "what sets us apart" - it suggests we are better than other clinicians and that is illegal. 
NO EMOTIVE PHOTOS PLEASE! 

Target Market(s)

clients wanting check background and contact information.

Industry/Entity Type

Mental Health

Requirements
Must have
• NEW LOGO
space for photographs
Old web page to complicated
http://wbtk.net.au/index.shtml
Should not have
• anything that flashes.

```html
<!DOCTYPE html>
<html lang="en">
<head>
<meta charset="utf-8">
<title>Bramblewood Mental Health</title>
<link href="https://fonts.googleapis.com/css2?family=Marcellus&family=Philosopher:wght@700&family=Source+Sans+3:wght@400;600;700&display=swap" rel="stylesheet">
<style>
  :root {
    --page: #ffffff;
    --brand: #1d4b6c;
    --brand-square: #2a6f93;
    --text-grey: #7a7a7a;
    --name-grey: #555555;
    --date-brown: #6b4424;
    --company-orange: #f4a93a;
    --blue-head-bg: #d1e8f5;
    --blue-head: #4aa3c8;
    --blue-panel: #eef6fc;
    --list-text: #6f8590;
    --cream-panel: #fdf5ea;
    --green-head-bg: #e3eddb;
    --green-head: #8aa860;
    --green-panel: #f0f5ec;
    --green-strong: #5a7a4a;
    --grey-head-bg: #d6e2e0;
    --grey-head: #7f9a96;
    --grey-panel: #f0f2f1;
    --gold-head-bg: #fde3bc;
    --gold-head: #9b7650;
    --rose-panel: #fbf2ef;
    --photo-dark: #4f4f4f;
    --photo-black: #111111;
  }
  * { box-sizing: border-box; margin: 0; padding: 0; }
  html, body { width: 927px; height: 1200px; overflow: hidden; background: var(--page); }
  body { position: relative; font-family: "Source Sans 3", sans-serif; color: var(--text-grey); }
  .abs { position: absolute; }

  .brand-square { left: 56px; top: 80px; width: 72px; height: 72px; background: var(--brand-square); border-radius: 4px; }
  .brand-name { left: 145px; top: 84px; color: var(--brand); font-family: "Source Sans 3", sans-serif; font-weight: 400; line-height: 1; }
  .brand-name .line-main { display: block; font-size: 36px; letter-spacing: 0.5px; }
  .brand-name .line-sub { display: block; font-size: 20px; letter-spacing: 1.5px; margin-top: 4px; }

  .contact { left: 58px; font-size: 14.5px; color: var(--text-grey); display: flex; align-items: center; gap: 9px; }
  .contact svg { width: 16px; height: 16px; flex: none; }
  .contact-phone { top: 187px; }
  .contact-address { top: 217px; }

  .portrait { width: 156px; height: 188px; background: #fff; padding: 10px 10px 14px; box-shadow: 2px 4px 8px rgba(0,0,0,0.35); }
  .portrait .photo { width: 100%; height: 100%; }
  .portrait-one { left: 461px; top: 71px; transform: rotate(3deg); }
  .portrait-one .photo { background: linear-gradient(160deg, #b0794c 0%, #6a4a3a 40%, #d9d2cc 75%, #3f5a7a 100%); }
  .portrait-two { left: 689px; top: 71px; transform: rotate(3deg); }
  .portrait-two .photo { background: linear-gradient(180deg, var(--photo-dark) 60%, var(--photo-black) 100%); }

  .person-name { top: 278px; font-family: "Marcellus", serif; font-size: 28px; color: var(--name-grey); width: 220px; text-align: center; }
  .person-one { left: 411px; }
  .person-two { left: 628px; }

  .section-head { height: 43px; border-radius: 4px; font-family: "Philosopher", serif; font-weight: 700; font-size: 28px; line-height: 43px; }
  .panel { border-radius: 4px; }
  .body-copy { font-size: 13.5px; line-height: 18px; color: var(--text-grey); }
  .body-copy b { font-weight: 700; color: #4a4a4a; }

  .experience-head { left: 58px; top: 275px; width: 258px; background: var(--blue-head-bg); color: var(--blue-head); text-align: center; }
  .experience-panel { left: 58px; top: 326px; width: 806px; height: 308px; background: var(--cream-panel); }
  .role-dates { left: 58px; width: 216px; text-align: right; }
  .role-dates .years { display: block; font-family: "Philosopher", serif; font-weight: 700; font-size: 30px; line-height: 32px; color: var(--date-brown); }
  .role-dates .company { display: block; font-weight: 700; font-size: 17px; line-height: 20px; color: var(--company-orange); letter-spacing: 0.3px; }
  .role-copy { left: 315px; width: 535px; }

  .assessment-head { left: 58px; top: 646px; width: 398px; background: var(--blue-head-bg); color: var(--blue-head); padding-left: 64px; }
  .assessment-panel { left: 58px; top: 698px; width: 398px; height: 256px; background: var(--blue-panel); }
  .condition-list { list-style: none; font-size: 14.5px; line-height: 21px; color: var(--list-text); }
  .condition-list li { margin-bottom: 9px; }
  .list-left { left: 83px; top: 723px; width: 170px; }
  .list-right { left: 275px; top: 723px; width: 170px; }

  .counselling-head { left: 467px; top: 646px; width: 397px; background: var(--green-head-bg); color: var(--green-head); padding-left: 68px; }
  .counselling-panel { left: 467px; top: 700px; width: 397px; height: 98px; background: var(--green-panel); }
  .counselling-copy { left: 490px; top: 716px; width: 355px; }
  .counselling-copy b { color: var(--green-strong); }

  .services-head { left: 467px; top: 807px; width: 397px; background: var(--grey-head-bg); color: var(--grey-head); padding-left: 68px; }
  .services-panel { left: 467px; top: 858px; width: 397px; height: 98px; background: var(--grey-panel); }
  .services-copy { left: 490px; top: 877px; width: 355px; }

  .gallery-head { left: 58px; top: 966px; width: 806px; background: var(--gold-head-bg); color: var(--gold-head); padding-left: 64px; }
  .gallery-panel { left: 58px; top: 1017px; width: 806px; height: 135px; background: var(--rose-panel); }
  .gallery-frame { top: 1030px; width: 137px; height: 107px; background: #fff; padding: 10px 10px 9px; border-radius: 3px; box-shadow: 0 1px 5px rgba(0,0,0,0.3); }
  .gallery-frame .photo { width: 100%; height: 100%; background: linear-gradient(180deg, var(--photo-dark) 60%, var(--photo-black) 100%); }
</style>
</head>
<body>
  <div class="abs brand-square"></div>
  <div class="abs brand-name"><span class="line-main">BRAMBLEWOOD</span><span class="line-sub">MENTAL HEALTH</span></div>

  <div class="abs contact contact-phone">
    <svg viewBox="0 0 16 16"><path d="M3.5 1.5l2.5 0 1 3.2-1.6 1.3c.8 1.8 2.2 3.2 4 4l1.3-1.6 3.2 1v2.6c0 .8-.7 1.4-1.5 1.3C7 12.6 3.4 9 2.2 3c-.1-.8.5-1.5 1.3-1.5z" fill="#8a9a9c"/></svg>
    <span>(08) 9312 4860 or 0431 558 207</span>
  </div>
  <div class="abs contact contact-address">
    <svg viewBox="0 0 16 16"><rect x="1.5" y="3.5" width="13" height="9" fill="none" stroke="#8a9a9c" stroke-width="1.3"/><path d="M1.5 3.5l6.5 5 6.5-5" fill="none" stroke="#8a9a9c" stroke-width="1.3"/></svg>
    <span>14 Wattlegrove Lane, MERIDEN 6031</span>
  </div>

  <div class="abs portrait portrait-one"><div class="photo" role="img" aria-label="Portrait photograph of Marissa Hale"></div></div>
  <div class="abs portrait portrait-two"><div class="photo" role="img" aria-label="Portrait photograph of Daniel Hale"></div></div>
  <div class="abs person-name person-one">Marissa Hale</div>
  <div class="abs person-name person-two">Daniel Hale</div>

  <div class="abs section-head experience-head">Experience</div>
  <div class="abs panel experience-panel"></div>

  <div class="abs role-dates" style="top:364px"><span class="years">1999/2006</span><span class="company">Company Name</span></div>
  <p class="abs body-copy role-copy" style="top:359px">Cras justo odio, dapibus ac facilisis in, <b>egestas eget quam</b>. Nulla vitae elit libero, a pharetra augue. Fusce dapibus, <b>tellus ac cursus commod</b> tortor mauris condimentum nibh, ut fermentum massa justo sit amet risus.</p>

  <div class="abs role-dates" style="top:454px"><span class="years">2006/2010</span><span class="company">Company Name</span></div>
  <p class="abs body-copy role-copy" style="top:452px">Cras justo odio, dapibus ac facilisis in, <b>egestas eget quam</b>. Nulla vitae elit libero, a pharetra augue. Fusce dapibus, <b>tellus ac cursus commod</b> tortor mauris condimentum nibh, ut fermentum massa justo sit amet risus.</p>

  <div class="abs role-dates" style="top:546px"><span class="years">2010/Now</span><span class="company">Company Name</span></div>
  <p class="abs body-copy role-copy" style="top:544px">Cras justo odio, dapibus ac facilisis in, <b>egestas eget quam</b>. Nulla vitae elit libero, a pharetra augue. Fusce dapibus, <b>tellus ac cursus commod</b> tortor mauris condimentum nibh, ut fermentum massa justo sit amet risus.</p>

  <div class="abs section-head assessment-head">Assessment</div>
  <div class="abs panel assessment-panel"></div>
  <ul class="abs condition-list list-left">
    <li>Phobias</li>
    <li>Panic</li>
    <li>Adjustment disorder</li>
    <li>Bereavement</li>
    <li>Post-traumatic stress disorder</li>
  </ul>
  <ul class="abs condition-list list-right">
    <li>Eating disorders</li>
    <li>Obsessive Compulsive disorder</li>
    <li>Bipolar disorder</li>
    <li>Schizophrenia</li>
    <li>Sleep problems</li>
    <li>Personality issues</li>
  </ul>

  <div class="abs section-head counselling-head">Counselling</div>
  <div class="abs panel counselling-panel"></div>
  <p class="abs body-copy counselling-copy">Cras justo odio, <b>dapibus ac</b> facilisis in, egestas eget quam. Nulla vitae elit libero, a pharetra augue. Fusce <b>dapibus, tellus ac cursus commodo</b>, tortor mauris condimentum.</p>

  <div class="abs section-head services-head">Other Services</div>
  <div class="abs panel services-panel"></div>
  <p class="abs body-copy services-copy">Cras justo odio, dapibus <b>ac facilisis in</b>, egestas eget quam. Nulla vitae elit libero, a <b>pharetra augue</b>. Fusce dapibus, tellus ac cursus commodo, tortor mauris condimentum.</p>

  <div class="abs section-head gallery-head">Gallery</div>
  <div class="abs panel gallery-panel"></div>
  <div class="abs gallery-frame" style="left:80px"><div class="photo" role="img" aria-label="Gallery photograph space"></div></div>
  <div class="abs gallery-frame" style="left:239px"><div class="photo" role="img" aria-label="Gallery photograph space"></div></div>
  <div class="abs gallery-frame" style="left:398px"><div class="photo" role="img" aria-label="Gallery photograph space"></div></div>
  <div class="abs gallery-frame" style="left:554px"><div class="photo" role="img" aria-label="Gallery photograph space"></div></div>
  <div class="abs gallery-frame" style="left:713px"><div class="photo" role="img" aria-label="Gallery photograph space"></div></div>
</body>
</html>
```